New Business Card Design Project

Details for my new Business Card Design Project will be added soon. Like a nice simple design

Target Market(s)

Home improvement

Industry/Entity Type

Home Improvement

Contact Information for Business Card

Roofing siding gutters additions garages decks

Requirements
Must have
• Phone 5074629183
• Email morvantgc@quellmail.com

```html
<!DOCTYPE html>
<html lang="en">
<head>
<meta charset="utf-8">
<title>Business Card – Home Improvement</title>
<link rel="stylesheet" href="https://fonts.googleapis.com/css2?family=Arimo:wght@700&display=swap">
<style>
  :root {
    --page-bg: #e4e4e6;
    --card-white: #f6f8f7;
    --brand-blue: #30318a;
    --text-light: #ffffff;
  }
  * { margin: 0; padding: 0; box-sizing: border-box; }
  html, body {
    width: 1200px;
    height: 1000px;
    overflow: hidden;
    background: var(--page-bg);
    font-family: "Arimo", Arial, sans-serif;
  }
  .business-card {
    position: absolute;
    left: 191px;
    top: 229px;
    width: 814px;
    height: 500px;
    background: var(--card-white);
    overflow: hidden;
  }
  .card-panel {
    position: absolute;
    inset: 0;
    width: 814px;
    height: 500px;
  }
  .contact {
    position: absolute;
    left: 73px;
    top: 84px;
    color: var(--brand-blue);
    font-weight: 700;
  }
  .contact-phone {
    font-size: 34px;
    line-height: 40px;
  }
  .contact-email {
    font-size: 24px;
    line-height: 30px;
    margin-top: 0;
  }
  .services {
    position: absolute;
    left: 484px;
    top: 128px;
    color: var(--text-light);
    font-weight: 700;
  }
  .services-title {
    font-size: 26px;
    line-height: 32px;
    letter-spacing: 0.5px;
    margin-bottom: 22px;
  }
  .services-list {
    list-style: none;
    font-size: 24px;
    line-height: 37px;
  }
</style>
</head>
<body>
  <div class="business-card">
    <svg class="card-panel" viewBox="0 0 814 500" aria-hidden="true">
      <polygon points="462,0 814,0 814,500 226,500" fill="var(--brand-blue)"/>
    </svg>

    <div class="contact">
      <p class="contact-phone">Ph: 507-462-9183</p>
      <p class="contact-email">morvantgc@quellmail.com</p>
    </div>

    <div class="services">
      <h2 class="services-title">OUR SERVICES</h2>
      <ul class="services-list">
        <li>Roofing</li>
        <li>Siding</li>
        <li>Gutter</li>
        <li>Additions</li>
        <li>Decks</li>
        <li>Handyman Services</li>
      </ul>
    </div>
  </div>
</body>
</html>
```